Torvik-Ellingsen Global AS

We need a design for our company including background pictures on our web (wix-template), redesign of logo and reports. Our company delivers personality test and services to clients when hiring staff or related to organizatonal developement.

Target Market(s)

Unisex, Age 30-50, managers in private corporations

Industry/Entity Type

Recruitment

Logo Text

Bygger laget sterkt (english translate: buids your team strong)

Number of Pages Required

1 page

Font styles to use
Sans Serif

Colors
add136
34a6d7
0255a3

Requirements
Must have
• The ideal designer will be the one to bring my narrative come to life. And it will have to include the testresults report and redesign (!) of my logo. Following the attached brief in ppt:
• - the testresult report
• - redesign logo
• - graphic elements in a maritime narrative
• - including the boat, the radar, 4 WINDs, the compass etc
Nice to have
• A strong narrative with a lot of elements.
• I really like the green color in the attached breif ;-)

```html
<!DOCTYPE html>
<html lang="no">
<head>
<meta charset="utf-8">
<title>Arbeidsstiler – Torvik-Ellingsen Global AS</title>
<link href="https://fonts.googleapis.com/css2?family=Raleway:wght@700;800;900&family=Roboto:wght@400&display=swap" rel="stylesheet">
<style>
  :root{
    --green:#617a34;
    --green-dark:#4f6a2a;
    --blue:#3aa8e0;
    --bar-blue:#41ade3;
    --ink:#2b2b2b;
    --box-line:#8a8f94;
    --dot:#a9b98e;
    --sky:#cfe5f3;
  }
  *{box-sizing:border-box;margin:0;padding:0}
  html,body{width:857px;height:1200px;overflow:hidden;background:#fff}
  .sheet{
    position:relative;width:857px;height:1200px;overflow:hidden;
    background:radial-gradient(ellipse 70% 60% at 50% 55%, #ffffff 0%, #f2f8fc 45%, var(--sky) 100%);
    font-family:'Roboto',Arial,sans-serif;color:var(--ink);
  }
  .header{position:absolute;left:0;top:0;width:857px;height:104px;background:#fff}
  .title{
    position:absolute;left:0;right:0;top:14px;text-align:center;
    font-family:'Raleway',Arial,sans-serif;font-weight:900;font-size:70px;
    letter-spacing:1px;color:var(--green);line-height:1;
  }
  .scallop{position:absolute;left:0;top:98px;width:857px;height:16px}

  .dots-h{position:absolute;height:0;border-top:3px dotted var(--dot)}
  .dots-v{position:absolute;width:0;border-left:3px dotted var(--dot)}

  .icon{position:absolute}
  .icon-fill{background:var(--blue);border-radius:6px;opacity:.9}

  .style-name{
    position:absolute;font-family:'Raleway',Arial,sans-serif;font-weight:800;
    font-size:29px;color:var(--blue);line-height:1;letter-spacing:.5px;
  }
  .rule{position:absolute;height:3px;background:var(--blue)}
  .rule::after{
    content:"";position:absolute;right:-7px;top:-4px;
    border-left:8px solid var(--blue);border-top:5.5px solid transparent;border-bottom:5.5px solid transparent;
  }
  .style-text{position:absolute;font-size:13px;line-height:17.2px;color:var(--ink)}
  .style-text.right{text-align:right}

  .brand{
    position:absolute;left:326px;top:334px;width:200px;height:80px;
    background:#fff;display:flex;align-items:center;justify-content:center;text-align:center;
    font-family:'Raleway',Arial,sans-serif;font-weight:800;font-size:17px;line-height:1.25;color:var(--green);
  }

  .battery{position:absolute;width:101px;height:50px}
  .metric{
    position:absolute;font-family:'Raleway',Arial,sans-serif;font-weight:800;font-size:30px;
    color:var(--green);line-height:1;text-align:center;width:300px;
  }

  .bar{
    position:absolute;top:816px;height:39px;width:380px;background:var(--bar-blue);
    color:#fff;font-family:'Raleway',Arial,sans-serif;font-weight:800;font-size:26px;
    display:flex;align-items:center;justify-content:center;letter-spacing:.5px;
  }
  .label{
    position:absolute;font-family:'Raleway',Arial,sans-serif;font-weight:700;font-size:17px;
    color:var(--ink);text-align:center;line-height:1;white-space:nowrap;transform:translateX(-50%);
  }
  .field{position:absolute;width:131px;height:33px;border:2px solid var(--box-line);background:rgba(255,255,255,.35)}
  .bracket{position:absolute;height:30px;border:2px solid #555;border-bottom:none}
</style>
</head>
<body>
<main class="sheet">
  <header class="header">
    <h1 class="title">ARBEIDSSTILER</h1>
  </header>
  <svg class="scallop" viewBox="0 0 857 16" preserveAspectRatio="none" aria-hidden="true">
    <defs>
      <pattern id="wave" width="14" height="16" patternUnits="userSpaceOnUse">
        <path d="M0 6 Q7 14 14 6" fill="none" stroke="#617a34" stroke-width="2.5"/>
      </pattern>
    </defs>
    <rect width="857" height="16" fill="url(#wave)"/>
  </svg>

  <!-- grid -->
  <div class="dots-v" style="left:425px;top:114px;height:534px"></div>
  <div class="dots-h" style="left:0;top:373px;width:857px"></div>
  <div class="dots-h" style="left:0;top:647px;width:857px"></div>
  <div class="dots-h" style="left:0;top:794px;width:857px"></div>
  <div class="dots-v" style="left:425px;top:796px;height:404px"></div>

  <div class="brand">Torvik-Ellingsen<br>Global AS</div>

  <!-- Worker -->
  <div class="icon icon-fill" role="img" aria-label="Illustrasjon av en arbeider med spade" style="left:114px;top:136px;width:96px;height:88px"></div>
  <div class="style-name" style="left:90px;top:229px">WORKER</div>
  <div class="rule" style="left:86px;top:257px;width:148px"></div>
  <p class="style-text" style="left:37px;top:268px;width:245px">Worker er effektiv og bekymret for ting som kan forsinke produksjonen. Kan være for kritisk i andres øyne. Faresignal: "martyrkultur".</p>

  <!-- Integrator -->
  <div class="icon icon-fill" role="img" aria-label="Illustrasjon av sammenkoblede puslespillbiter" style="left:660px;top:136px;width:88px;height:88px"></div>
  <div class="style-name" style="left:607px;top:229px">INTEGRATOR</div>
  <div class="rule" style="left:596px;top:257px;width:216px"></div>
  <p class="style-text right" style="left:575px;top:268px;width:246px">Integrator er opptatt av menneskene og involverer mange i å løse oppgaven. Kan være for avhengig av andres støtte. Faresignal: ”kappevender”.</p>

  <!-- Navigator -->
  <svg class="icon" style="left:111px;top:413px" width="88" height="88" viewBox="0 0 88 88" role="img" aria-label="Kompass">
    <circle cx="44" cy="44" r="39" fill="none" stroke="#3aa8e0" stroke-width="6"/>
    <path d="M24 22 L50 40 L66 68 L40 50 Z" fill="#3aa8e0"/>
    <circle cx="45" cy="45" r="4" fill="#fff"/>
  </svg>
  <div class="style-name" style="left:66px;top:508px">NAVIGATOR</div>
  <div class="rule" style="left:56px;top:535px;width:204px"></div>
  <p class="style-text" style="left:37px;top:546px;width:260px">Navigator peker retning. Han tror alt er mulig og kan være for bred i sin tilnærming – overser (viktige) detaljer. Faresignal: "Brannstifter".</p>

  <!-- Discipline -->
  <div class="icon icon-fill" role="img" aria-label="Illustrasjon av skriveplate med penn" style="left:671px;top:414px;width:87px;height:86px"></div>
  <div class="style-name" style="left:629px;top:509px">DICIPLINE</div>
  <div class="rule" style="left:624px;top:535px;width:162px"></div>
  <p class="style-text right" style="left:560px;top:546px;width:258px">Diciplin er forutsigbar og overholder sine ansvarsområder. Kan være for avhengig av stabilitet. Faresignal: "byråkratisk kultur".</p>

  <!-- Batteries -->
  <svg class="battery" style="left:139px;top:677px" viewBox="0 0 101 50" aria-hidden="true">
    <rect x="3" y="3" width="84" height="44" rx="7" fill="none" stroke="#617a34" stroke-width="6"/>
    <rect x="88" y="15" width="10" height="20" rx="2" fill="#617a34"/>
    <path d="M12 12 H64 L70 38 H12 Z" fill="#617a34"/>
  </svg>
  <div class="metric" style="left:36px;top:742px">ENERGY</div>

  <svg class="battery" style="left:604px;top:677px" viewBox="0 0 101 50" aria-hidden="true">
    <rect x="3" y="3" width="84" height="44" rx="7" fill="none" stroke="#617a34" stroke-width="6"/>
    <rect x="88" y="15" width="10" height="20" rx="2" fill="#617a34"/>
    <path d="M12 12 H28 L34 38 H12 Z" fill="#617a34"/>
  </svg>
  <div class="metric" style="left:501px;top:742px">PROBLEM SOLVE</div>

  <!-- Listing -->
  <div class="bar" style="left:21px">LISTING</div>
  <div class="label" style="left:212px;top:883px">ENERGI (0-100)</div>
  <div class="field" style="left:147px;top:907px"></div>
  <div class="label" style="left:212px;top:965px">PROBLEMLØSNINGSEVNE (0-100)</div>
  <div class="field" style="left:147px;top:987px"></div>
  <div class="label" style="left:211px;top:1052px">LYTTE</div>
  <div class="bracket" style="left:98px;top:1077px;width:231px"></div>
  <div class="label" style="left:102px;top:1113px">EMPATI</div>
  <div class="label" style="left:325px;top:1113px">PROFESJONELL</div>
  <div class="field" style="left:35px;top:1134px"></div>
  <div class="field" style="left:260px;top:1134px"></div>

  <!-- Sende -->
  <div class="bar" style="left:455px">SENDE</div>
  <div class="label" style="left:650px;top:883px">ENERGI (0-100)</div>
  <div class="field" style="left:584px;top:907px"></div>
  <div class="label" style="left:650px;top:965px">PROBLEMLØSNINGSEVNE (0-100)</div>
  <div class="field" style="left:584px;top:987px"></div>
  <div class="label" style="left:657px;top:1052px">SENDE</div>
  <div class="bracket" style="left:544px;top:1077px;width:232px"></div>
  <div class="label" style="left:555px;top:1113px">OVERBEVISNINGSEVNE</div>
  <div class="label" style="left:767px;top:1113px">AUTORITET</div>
  <div class="field" style="left:488px;top:1134px"></div>
  <div class="field" style="left:705px;top:1134px"></div>
</main>
</body>
</html>
```